Bakery Business Cards

We are in need of business cards for our bakery business--something non-generic that reflects our business and will stand out. We are a wholesale bakery that primarily services in-store bakeries, casinos, schools, distributors, and fund-raising companies. The family business was founded in 1960. (www.dorvalbakehouse.example)

```html
<!DOCTYPE html>
<html lang="en">
<head>
<meta charset="utf-8">
<title>Dorval Bakehouse – Business Cards</title>
<link rel="stylesheet" href="https://fonts.googleapis.com/css2?family=Libre+Baskerville:wght@400;700&display=swap">
<style>
  :root {
    --page-bg: #c9c9cc;
    --card-white: #ffffff;
    --brand-blue: #3a4ea0;
    --brand-blue-light: #7886c2;
    --text-grey: #555555;
    --card-shadow: rgba(0, 0, 0, 0.22);
  }
  * { margin: 0; padding: 0; box-sizing: border-box; }
  html, body {
    width: 1200px;
    height: 1178px;
    overflow: hidden;
    background: var(--page-bg);
    font-family: "Libre Baskerville", Georgia, serif;
  }
  .canvas {
    position: relative;
    width: 1200px;
    height: 1178px;
    display: flex;
    justify-content: center;
    align-items: center;
    gap: 70px;
  }
  .card {
    position: relative;
    width: 430px;
    height: 740px;
    border-radius: 38px;
    overflow: hidden;
    box-shadow: 0 18px 40px var(--card-shadow);
  }

  /* Front */
  .card--front { background: var(--card-white); }
  .brand-name {
    font-weight: 700;
    text-align: center;
    line-height: 1.15;
    letter-spacing: 0.5px;
  }
  .card--front .brand-name {
    position: absolute;
    top: 120px;
    left: 0;
    right: 0;
    font-size: 40px;
    color: var(--brand-blue);
  }
  .name-band {
    position: absolute;
    top: 330px;
    left: 0;
    right: 0;
    height: 112px;
    background: linear-gradient(90deg, var(--brand-blue-light), var(--brand-blue));
    color: var(--card-white);
    padding: 20px 0 0 70px;
  }
  .person-name { font-size: 34px; line-height: 1.2; }
  .person-title { font-size: 19px; margin-top: 4px; }
  .address {
    position: absolute;
    top: 540px;
    left: 70px;
    font-size: 18px;
    line-height: 1.45;
    color: var(--text-grey);
  }
  .contact-list {
    position: absolute;
    top: 618px;
    left: 70px;
    list-style: none;
    font-size: 18px;
    line-height: 1.45;
    color: var(--text-grey);
  }
  .contact-list li { display: flex; align-items: center; gap: 12px; white-space: nowrap; }
  .contact-list svg { width: 18px; height: 18px; flex: none; fill: var(--brand-blue); }
  .contact-list .web { font-size: 16px; }
  .contact-list .email { font-size: 16px; }

  /* Back */
  .card--back {
    background: linear-gradient(135deg, var(--brand-blue-light) 0%, var(--brand-blue) 55%, var(--brand-blue) 100%);
  }
  .back-stripe {
    position: absolute;
    top: 0;
    left: 160px;
    width: 108px;
    height: 420px;
    background: var(--card-white);
  }
  .card--back .brand-name {
    position: absolute;
    top: 525px;
    left: 0;
    right: 0;
    font-size: 40px;
    color: var(--card-white);
  }
</style>
</head>
<body>
<main class="canvas">
  <section class="card card--front" aria-label="Business card front">
    <div class="brand-name">Dorval<br>Bakehouse</div>
    <div class="name-band">
      <div class="person-name">Maren Holt</div>
      <div class="person-title">Partner &amp; CEO</div>
    </div>
    <address class="address" style="font-style:normal">
      1570 Ledger Ave<br>Riverton, OK 74000
    </address>
    <ul class="contact-list">
      <li>
        <svg viewBox="0 0 24 24" aria-hidden="true"><path d="M6.6 10.8a15.1 15.1 0 0 0 6.6 6.6l2.2-2.2a1 1 0 0 1 1-.25 11.4 11.4 0 0 0 3.6.57 1 1 0 0 1 1 1V20a1 1 0 0 1-1 1A17 17 0 0 1 3 4a1 1 0 0 1 1-1h3.5a1 1 0 0 1 1 1c0 1.25.2 2.45.57 3.57a1 1 0 0 1-.25 1z"/></svg>
        (555)010-4821
      </li>
      <li class="email">
        <svg viewBox="0 0 24 24" aria-hidden="true"><path d="M2 5h20v14H2zm2 2v.5l8 5 8-5V7l-8 5z"/></svg>
        sales@dorvalbakehouse.example
      </li>
      <li class="web">
        <svg viewBox="0 0 24 24" aria-hidden="true"><path d="M12 2a10 10 0 1 0 0 20 10 10 0 0 0 0-20zm6.9 6h-3a15.6 15.6 0 0 0-1.3-3.9A8 8 0 0 1 18.9 8zM12 4c.8 1.1 1.5 2.5 1.9 4h-3.8c.4-1.5 1.1-2.9 1.9-4zM4.3 14a8 8 0 0 1 0-4h3.4a16 16 0 0 0 0 4zm.8 2h3a15.6 15.6 0 0 0 1.3 3.9A8 8 0 0 1 5.1 16zm3-8h-3a8 8 0 0 1 4.3-3.9C8.8 5.3 8.4 6.6 8.1 8zM12 20c-.8-1.1-1.5-2.5-1.9-4h3.8c-.4 1.5-1.1 2.9-1.9 4zm2.3-6H9.7a14.5 14.5 0 0 1 0-4h4.6a14.5 14.5 0 0 1 0 4zm.3 5.9c.6-1.2 1-2.5 1.3-3.9h3a8 8 0 0 1-4.3 3.9zm1.7-5.9a16 16 0 0 0 0-4h3.4a8 8 0 0 1 0 4z"/></svg>
        www.dorvalbakehouse.example
      </li>
    </ul>
  </section>

  <section class="card card--back" aria-label="Business card back">
    <div class="back-stripe"></div>
    <div class="brand-name">Dorval<br>Bakehouse</div>
  </section>
</main>
</body>
</html>
```